first fantastic look and impression

We are looking for a concept for letterhead, business card, emailfooter and template for invoices or offers for our company in the consultation business.
The dancer is a symbol who we are: it looks simple, but there is a lot of hard work and many years of training in this movement. The look is also what we want: elegant, modern, strong, with a touch of extravaganza
Target Market(s)
Hotelbusiness , Consulting
Font styles to use
Sans Serif
Other font styles liked:
- please give us a option we are open
Requirements
Must have
- We are not typical consultants but sparring partners and coaches for the hotel and that should also be expressed in the design. Maybe there is an icon that supports the whole thing. We are more modern and bolder than our industry colleagues.
we are modern, fresh, agile, fast
Nice to have
- a icon

```html
<!DOCTYPE html>
<html lang="en">
<head>
<meta charset="utf-8">
<title>Lindholm+Partner – Stationery</title>
<link rel="stylesheet" href="https://fonts.googleapis.com/css2?family=Montserrat:wght@400;500;600;700&family=Roboto:wght@400;500&display=swap">
<style>
  :root{
    --ink:#111214;
    --paper:#ffffff;
    --paper-warm:#f7f6f3;
    --scene-cool:#d6dadc;
    --scene-light:#e4e5e6;
    --scene-env:#e9e9e9;
    --rule:#8a8c90;
    --row:#e6e7e9;
    --muted:#5b5e63;
  }
  *{box-sizing:border-box;margin:0;padding:0}
  html,body{width:1200px;height:4344px;overflow:hidden}
  body{font-family:"Roboto",sans-serif;color:var(--ink);background:var(--paper);position:relative}
  .section{position:absolute;left:0;width:1200px}
  .section--cards-a{top:0;height:1045px;background:var(--scene-cool)}
  .section--cards-b{top:1045px;height:1053px;background:var(--scene-cool)}
  .section--stationery{top:2098px;height:775px;background:var(--scene-light)}
  .section--envelopes{top:2873px;height:792px;background:var(--scene-env)}
  .section--footers{top:3665px;height:679px;background:var(--paper)}

  .wordmark{font-family:"Montserrat",sans-serif;font-weight:500;letter-spacing:.06em;text-transform:uppercase;white-space:nowrap}

  .icon{width:1em;height:1em;flex:none}
  .contact-list{list-style:none}
  .contact-list li{display:flex;align-items:center;gap:.45em;line-height:1.35}

  /* business cards */
  .card{position:absolute;width:500px;height:290px;box-shadow:0 14px 30px rgba(0,0,0,.18)}
  .card--back{left:590px;top:260px;background:var(--ink);border-bottom:6px solid #b08d4c;display:flex;align-items:center;justify-content:center}
  .card--back .wordmark{color:var(--paper);font-size:30px}
  .card--front{left:140px;top:400px;background:var(--paper-warm);padding:40px 44px}
  .card--front .wordmark{font-size:18px}
  .card__name{margin-top:70px;font-family:"Montserrat",sans-serif;font-weight:700;font-size:17px;text-transform:uppercase}
  .card__dash{width:16px;height:2px;background:var(--ink);margin:10px 0 10px}
  .card .contact-list{font-size:14px}

  /* stationery pages */
  .page{position:absolute;top:110px;width:413px;height:572px;background:var(--paper);box-shadow:0 2px 8px rgba(0,0,0,.12);padding:34px 26px;font-size:8px}
  .page--invoice{left:163px}
  .page--letter{left:613px}
  .page__head{display:flex;justify-content:space-between;align-items:flex-start}
  .page__head .wordmark{font-size:12px;margin-top:8px}
  .page__head .contact-list{font-size:7.5px}
  .invoice__title{display:flex;justify-content:space-between;margin-top:44px;font-family:"Montserrat",sans-serif;font-weight:700;font-size:10px}
  .invoice__title span:last-child{font-size:7px;font-weight:600;margin-right:60px}
  .field{display:flex;gap:4px;font-size:6.5px;margin-top:6px;align-items:flex-end}
  .field__line{flex:1;border-bottom:1px solid var(--rule);height:7px}
  .invoice__table{width:100%;border-collapse:collapse;margin-top:14px;border:1px solid var(--rule);font-size:6.5px}
  .invoice__table th{background:var(--ink);color:var(--paper);font-family:"Montserrat",sans-serif;font-weight:600;height:16px}
  .invoice__table td{height:16.5px;border-left:1px solid var(--rule)}
  .invoice__table tr:nth-child(even) td{background:var(--row)}
  .invoice__foot{display:flex;justify-content:space-between;margin-top:0}
  .payment{display:flex;gap:8px;font-size:5.5px;margin-top:6px}
  .payment span{display:flex;align-items:center;gap:2px}
  .payment span::before{content:"";width:6px;height:6px;border:1px solid var(--rule)}
  .note{font-size:5.5px;color:var(--muted);margin-top:14px;line-height:1.4}
  .totals{border-collapse:collapse;font-size:5.5px;width:124px}
  .totals td{border:1px solid var(--rule);height:13px;padding-left:6px;font-family:"Montserrat",sans-serif;font-weight:600}
  .totals td+td{width:62px}
  .letter__body{margin-top:50px;font-size:6.5px;line-height:1.55;color:#3a3c40}
  .letter__body p{margin-bottom:9px}
  .signature{width:44px;height:30px;background:linear-gradient(135deg,#f0f0f0,#dcdcdc);margin-top:6px}

  /* envelopes */
  .envelope{position:absolute;width:640px;height:300px;background:var(--paper);box-shadow:0 18px 30px rgba(0,0,0,.14)}
  .envelope--back{left:440px;top:110px;overflow:hidden}
  .envelope__flap{height:90px;background:var(--ink);display:flex;align-items:center;justify-content:center}
  .envelope__seal{width:46px;height:46px;border-radius:50%;background:var(--paper);border:2px solid #c9c9c9}
  .envelope--front{left:120px;top:380px;padding:36px 40px}
  .envelope--front .wordmark{font-size:16px}
  .envelope__address{font-size:12px;margin-top:4px;color:#333}

  /* email footers */
  .signature-block{position:absolute;left:229px;width:743px;height:182px;background:var(--paper);box-shadow:4px 6px 12px rgba(0,0,0,.3);padding:40px 44px;display:flex;justify-content:space-between}
  .signature-block--one{top:147px}
  .signature-block--two{top:352px}
  .signature-block__name{font-family:"Montserrat",sans-serif;font-weight:700;font-size:19px;text-transform:uppercase}
  .signature-block .card__dash{margin:9px 0 8px}
  .signature-block .contact-list{font-size:16px}
  .signature-block .wordmark{font-size:17px;margin-top:30px}
</style>
</head>
<body>
<svg width="0" height="0" style="position:absolute" aria-hidden="true">
  <symbol id="i-pin" viewBox="0 0 20 20"><circle cx="10" cy="10" r="10" fill="currentColor"/><path d="M10 4.5a3.6 3.6 0 0 0-3.6 3.6c0 2.7 3.6 6.9 3.6 6.9s3.6-4.2 3.6-6.9A3.6 3.6 0 0 0 10 4.5zm0 5a1.4 1.4 0 1 1 0-2.8 1.4 1.4 0 0 1 0 2.8z" fill="#fff"/></symbol>
  <symbol id="i-phone" viewBox="0 0 20 20"><circle cx="10" cy="10" r="10" fill="currentColor"/><path d="M7 5l2 2.6-1.1 1.4a6 6 0 0 0 3 3l1.4-1.1L15 13l-1 2c-4.2 0-9-4.8-9-9z" fill="#fff"/></symbol>
  <symbol id="i-mail" viewBox="0 0 20 20"><circle cx="10" cy="10" r="10" fill="currentColor"/><rect x="5" y="6.5" width="10" height="7" fill="#fff"/><path d="M5 6.5l5 4 5-4" stroke="currentColor" fill="none" stroke-width="1"/></symbol>
  <symbol id="i-web" viewBox="0 0 20 20"><circle cx="10" cy="10" r="10" fill="currentColor"/><circle cx="10" cy="10" r="5" fill="none" stroke="#fff" stroke-width="1.2"/><path d="M5 10h10M10 5c-2.5 3-2.5 7 0 10M10 5c2.5 3 2.5 7 0 10" fill="none" stroke="#fff" stroke-width="1"/></symbol>
</svg>

<section class="section section--cards-a">
  <div class="card card--back"><span class="wordmark">Lindholm+Partner</span></div>
  <div class="card card--front">
    <span class="wordmark">Lindholm+Partner</span>
    <p class="card__name">Sabine Lindholm</p>
    <div class="card__dash"></div>
    <ul class="contact-list">
      <li><svg class="icon"><use href="#i-pin"/></svg>6850 Arlen / Feldweg 12</li>
      <li><svg class="icon"><use href="#i-phone"/></svg>+43 660 1234567</li>
      <li><svg class="icon"><use href="#i-mail"/></svg>sl@lindholmpartner.com</li>
      <li><svg class="icon"><use href="#i-web"/></svg>lindholmpartner.com</li>
    </ul>
  </div>
</section>

<section class="section section--cards-b">
  <div class="card card--back"><span class="wordmark">Lindholm+Partner</span></div>
  <div class="card card--front">
    <span class="wordmark">Lindholm+Partner</span>
    <p class="card__name">Tobias Lindholm</p>
    <div class="card__dash"></div>
    <ul class="contact-list">
      <li><svg class="icon"><use href="#i-pin"/></svg>6850 Arlen / Feldweg 12</li>
      <li><svg class="icon"><use href="#i-phone"/></svg>+43 660 7654321</li>
      <li><svg class="icon"><use href="#i-mail"/></svg>tl@lindholmpartner.com</li>
      <li><svg class="icon"><use href="#i-web"/></svg>lindholmpartner.com</li>
    </ul>
  </div>
</section>

<section class="section section--stationery">
  <article class="page page--invoice">
    <header class="page__head">
      <span class="wordmark">Lindholm+Partner</span>
      <ul class="contact-list">
        <li><svg class="icon"><use href="#i-pin"/></svg>6850 Arlen / Feldweg 12</li>
        <li><svg class="icon"><use href="#i-phone"/></svg>+43 5500 10020</li>
        <li><svg class="icon"><use href="#i-mail"/></svg>info@lindholmpartner.com</li>
        <li><svg class="icon"><use href="#i-web"/></svg>lindholmpartner.com</li>
      </ul>
    </header>
    <div class="invoice__title"><span>INVOICE # :</span><span>DATE :</span></div>
    <div class="field"><span>Customer :</span><span class="field__line"></span></div>
    <div class="field"><span>Address :</span><span class="field__line"></span></div>
    <div class="field"><span>Phone :</span><span class="field__line"></span><span>Fax :</span><span class="field__line"></span></div>
    <table class="invoice__table">
      <thead><tr><th style="width:48px">QTY</th><th>DESCRIPTION</th><th style="width:62px">PRICE</th><th style="width:62px">AMOUNT</th></tr></thead>
      <tbody>
        <tr><td></td><td></td><td></td><td></td></tr><tr><td></td><td></td><td></td><td></td></tr>
        <tr><td></td><td></td><td></td><td></td></tr><tr><td></td><td></td><td></td><td></td></tr>
        <tr><td></td><td></td><td></td><td></td></tr><tr><td></td><td></td><td></td><td></td></tr>
        <tr><td></td><td></td><td></td><td></td></tr><tr><td></td><td></td><td></td><td></td></tr>
        <tr><td></td><td></td><td></td><td></td></tr><tr><td></td><td></td><td></td><td></td></tr>
        <tr><td></td><td></td><td></td><td></td></tr><tr><td></td><td></td><td></td><td></td></tr>
        <tr><td></td><td></td><td></td><td></td></tr><tr><td></td><td></td><td></td><td></td></tr>
      </tbody>
    </table>
    <div class="invoice__foot">
      <div>
        <div class="payment"><span>VISA</span><span>MC</span><span>DEBIT</span><span>CASH</span><span>CHEQUE</span></div>
        <p class="note">Signature indicates<br>Acceptance of Price and term</p>
      </div>
      <table class="totals">
        <tr><td>SUB TOTAL</td><td></td></tr>
        <tr><td>GST #</td><td></td></tr>
        <tr><td>SUBTOTAL</td><td></td></tr>
      </table>
    </div>
  </article>

  <article class="page page--letter">
    <header class="page__head">
      <span class="wordmark">Lindholm+Partner</span>
      <ul class="contact-list">
        <li><svg class="icon"><use href="#i-pin"/></svg>6850 Arlen / Feldweg 12</li>
        <li><svg class="icon"><use href="#i-phone"/></svg>+43 5500 10020</li>
        <li><svg class="icon"><use href="#i-mail"/></svg>info@lindholmpartner.com</li>
        <li><svg class="icon"><use href="#i-web"/></svg>lindholmpartner.com</li>
      </ul>
    </header>
    <div class="letter__body">
      <p>Dear customer,</p>
      <p>Thank you for your trust in our work. We support hotel teams as sparring partners and coaches, with clear goals, honest feedback and steady practice that turns good service into lasting quality for every guest.</p>
      <p>Our next session will focus on front office routines, guest journeys and the small gestures that make a stay memorable. Please share your questions in advance so we can prepare well.</p>
      <p>We look forward to working with you and your team again and to seeing the progress grow step by step.</p>
      <p>Yours Sincerely,</p>
      <div class="signature" role="img" aria-label="Handwritten signature"></div>
    </div>
  </article>
</section>

<section class="section section--envelopes">
  <div class="envelope envelope--back">
    <div class="envelope__flap"><span class="envelope__seal"></span></div>
  </div>
  <div class="envelope envelope--front">
    <span class="wordmark">Lindholm+Partner</span>
    <p class="envelope__address">6850 Arlen / Feldweg 12</p>
  </div>
</section>

<section class="section section--footers">
  <div class="signature-block signature-block--one">
    <div>
      <p class="signature-block__name">Sabine Lindholm</p>
      <div class="card__dash"></div>
      <ul class="contact-list">
        <li><svg class="icon"><use href="#i-pin"/></svg>6850 Arlen / Feldweg 12</li>
        <li><svg class="icon"><use href="#i-phone"/></svg>+43 660 1234567</li>
        <li><svg class="icon"><use href="#i-mail"/></svg>sl@lindholmpartner.com</li>
        <li><svg class="icon"><use href="#i-web"/></svg>lindholmpartner.com</li>
      </ul>
    </div>
    <span class="wordmark">Lindholm+Partner</span>
  </div>
  <div class="signature-block signature-block--two">
    <div>
      <p class="signature-block__name">Tobias Lindholm</p>
      <div class="card__dash"></div>
      <ul class="contact-list">
        <li><svg class="icon"><use href="#i-pin"/></svg>6850 Arlen / Feldweg 12</li>
        <li><svg class="icon"><use href="#i-phone"/></svg>+43 660 7654321</li>
        <li><svg class="icon"><use href="#i-mail"/></svg>tl@lindholmpartner.com</li>
        <li><svg class="icon"><use href="#i-web"/></svg>lindholmpartner.com</li>
      </ul>
    </div>
    <span class="wordmark">Lindholm+Partner</span>
  </div>
</section>
</body>
</html>
```